Korvane - Business Card Design

Design a modern masculine business card for our business

Target Market(s)

Private Market

Industry/Entity Type

Construction

Contact Information for Business Card

Company Name - Name of Person - Address - email address - contact number

Font styles to use
Serif
Sans Serif

Colors
0094D4
00A9DD
6FCCEA
C7EBF8
E9F6FB
00AB8E
00BBA5
67D7C9
C6EFE9
E9F9F6
F0912C
F2A743
F7CA91
FBE8D2
FDF5EE

Requirements
Must have
• Use company logo provided
Nice to have
• Company Logo

```html
<!DOCTYPE html>
<html lang="en">
<head>
<meta charset="utf-8">
<title>Korvane Business Card</title>
<link href="https://fonts.googleapis.com/css2?family=Montserrat:wght@400;500;700;800&display=swap" rel="stylesheet">
<style>
  :root {
    --bg: #e4e4e4;
    --card-light: #f4f2f0;
    --card-dark: #363636;
    --orange: #ee7a35;
    --ink: #333333;
    --muted: #555555;
  }
  html, body {
    margin: 0;
    width: 1200px;
    height: 853px;
    overflow: hidden;
    background: var(--bg);
    font-family: "Montserrat", sans-serif;
  }
  .canvas { position: relative; width: 1200px; height: 853px; }
  .card {
    position: absolute;
    top: 276px;
    width: 520px;
    height: 300px;
    border-radius: 22px;
    overflow: hidden;
    box-shadow: 0 6px 18px rgba(0,0,0,0.12);
  }
  .card--front { left: 50px; background: var(--card-light); }
  .card--back { left: 630px; background: var(--card-dark); }
  .card__shapes { position: absolute; inset: 0; }

  .brand {
    position: absolute;
    display: flex;
    align-items: center;
    gap: 8px;
    font-weight: 800;
    letter-spacing: 0.5px;
    white-space: nowrap;
  }
  .brand__square { display: block; background: var(--orange); }
  .card--front .brand { left: 34px; top: 34px; color: var(--card-dark); font-size: 18px; }
  .card--front .brand__square { width: 12px; height: 12px; }
  .card--back .brand {
    left: 0; right: 0; top: 130px;
    justify-content: center;
    color: #ffffff; font-size: 28px;
  }
  .card--back .brand__square { width: 20px; height: 20px; }

  .person { position: absolute; right: 32px; top: 84px; text-align: right; }
  .person__name { margin: 0; font-size: 19px; font-weight: 700; color: var(--ink); }
  .person__name span { color: var(--orange); }
  .person__role { margin: 2px 0 0; font-size: 11px; color: var(--muted); }
  .contact {
    position: absolute;
    right: 32px;
    top: 140px;
    margin: 0;
    padding: 0;
    list-style: none;
    font-size: 10.5px;
    color: var(--muted);
  }
  .contact li {
    display: flex;
    align-items: center;
    justify-content: flex-end;
    gap: 8px;
    margin-bottom: 6px;
    line-height: 1.3;
  }
  .contact svg { width: 11px; height: 11px; flex: none; fill: var(--orange); }
</style>
</head>
<body>
<main class="canvas">

  <section class="card card--front" aria-label="Business card front">
    <svg class="card__shapes" viewBox="0 0 520 300" aria-hidden="true">
      <polygon points="0,170 190,170 240,236 520,236 520,300 0,300" fill="var(--card-dark)"/>
      <rect x="0" y="160" width="150" height="5" fill="var(--orange)"/>
      <rect x="0" y="292" width="520" height="8" fill="var(--orange)"/>
    </svg>
    <div class="brand"><span class="brand__square"></span>Korvane Construction, Inc</div>
    <div class="person">
      <h1 class="person__name">Name Of <span>Person</span></h1>
      <p class="person__role">General Manager</p>
    </div>
    <ul class="contact">
      <li>+000 123 456 7890
        <svg viewBox="0 0 24 24"><path d="M6.6 10.8a15.1 15.1 0 0 0 6.6 6.6l2.2-2.2a1 1 0 0 1 1-.25 11.4 11.4 0 0 0 3.6.57 1 1 0 0 1 1 1V20a1 1 0 0 1-1 1A17 17 0 0 1 3 4a1 1 0 0 1 1-1h3.5a1 1 0 0 1 1 1c0 1.25.2 2.45.57 3.57a1 1 0 0 1-.25 1z"/></svg>
      </li>
      <li>yourmail@name.com
        <svg viewBox="0 0 24 24"><path d="M2 5h20v14H2z M2 5l10 8 10-8" stroke="#fff" stroke-width="1.5"/></svg>
      </li>
      <li>your street name here<br>New York City, Zip - 000
        <svg viewBox="0 0 24 24"><path d="M12 2a7 7 0 0 0-7 7c0 5 7 13 7 13s7-8 7-13a7 7 0 0 0-7-7zm0 9.5A2.5 2.5 0 1 1 12 6.5a2.5 2.5 0 0 1 0 5z"/></svg>
      </li>
    </ul>
  </section>

  <section class="card card--back" aria-label="Business card back">
    <svg class="card__shapes" viewBox="0 0 520 300" aria-hidden="true">
      <rect x="0" y="44" width="120" height="6" fill="var(--orange)"/>
      <rect x="400" y="250" width="120" height="6" fill="var(--orange)"/>
    </svg>
    <div class="brand"><span class="brand__square"></span>Korvane Construction, Inc</div>
  </section>

</main>
</body>
</html>
```